Business Card for a recruitment agency specializing in engineers and geeks.

I am looking to create Business Card Design for my company.
That
## Company name:
Quorvant Inc.
Quorvant is a term coined from the following concepts.
1. geek + engineer
2. geek utopia
## Company Description:
The concept of the company is to be a recruitment agency that creates a paradise for geeky engineers. We want to be a place where engineers can have more freedom and ideal career support.
# Target.
The noun itself is often given to companies that want to hire engineers, geeks, and IT-related personnel, so it would be nice to get the impression that this company seems to have good engineers and IT personnel. There are many occasions where I meet with the human resources department, president, or senior management and give it to them.
# Atmosphere
We are happy with simplicity, but with an impact that will help people remember the company. The logo is based on a dinosaur that does programming, so it should be somewhat playful, but since it will basically be used in a business setting, please don't make it too silly.
# About the logo
See the attached files. The company logo represents our engineers smiling upward because of our work, with the motif of a dinosaur doing programming.
## Color
We will leave the color scheme to you, but since the logo is in black and white, colors with such a taste would fit well.
## file format
ai, psd, png, svg
Industry/Entity Type
human resource and employment agency
Contact Information for Business Card
Company name, address, email, tel, URL,logo
Colors
Designer to choose colors to be used in the design.

```html
<!DOCTYPE html>
<html lang="en">
<head>
<meta charset="utf-8">
<title>Quorvant Business Card</title>
<link rel="stylesheet" href="https://fonts.googleapis.com/css2?family=Roboto:wght@400;500;700&display=swap">
<style>
  :root {
    --backdrop: #2b2b2b;
    --card-top: #f3f3f3;
    --card-bottom: #dedede;
    --ink: #111111;
    --ink-soft: #2a2a2a;
    --icon: #8a8a8a;
  }
  * { margin: 0; padding: 0; box-sizing: border-box; }
  html, body {
    width: 1200px;
    height: 1138px;
    overflow: hidden;
    background: var(--backdrop);
    font-family: "Roboto", Arial, sans-serif;
    color: var(--ink);
  }
  .card {
    position: absolute;
    width: 620px;
    height: 375px;
    border-radius: 16px;
    background: linear-gradient(180deg, var(--card-top), var(--card-bottom));
  }
  .card--front { left: 274px; top: 186px; }
  .card--back { left: 276px; top: 608px; }

  .brand {
    position: absolute;
    display: flex;
    align-items: center;
    gap: 14px;
    font-weight: 500;
    color: var(--ink);
    letter-spacing: 0.5px;
  }
  .brand__mark {
    background: var(--ink);
    display: block;
  }
  .brand--hero {
    left: 0; right: 0; top: 132px;
    justify-content: center;
    font-size: 48px;
  }
  .brand--hero .brand__mark { width: 34px; height: 34px; }
  .brand--header {
    right: 36px; top: 58px;
    font-size: 34px;
  }
  .brand--header .brand__mark { width: 26px; height: 26px; }

  .front__url {
    position: absolute;
    left: 0; right: 0; top: 333px;
    display: flex;
    justify-content: center;
    align-items: center;
    gap: 16px;
    font-size: 15px;
    color: var(--ink-soft);
  }
  .front__rule { width: 60px; height: 2px; background: var(--ink); }

  .person {
    position: absolute;
    left: 36px; top: 260px;
    display: flex;
    align-items: baseline;
    gap: 12px;
  }
  .person__name { font-size: 21px; font-weight: 700; color: var(--ink-soft); }
  .person__title { font-size: 15px; color: var(--ink-soft); }

  .contact {
    position: absolute;
    left: 36px;
    display: flex;
    align-items: center;
    gap: 10px;
    font-size: 15px;
    color: var(--ink-soft);
  }
  .contact--row1 { top: 296px; }
  .contact--row2 { top: 323px; }
  .contact__item { display: flex; align-items: center; gap: 10px; margin-right: 8px; }
  .contact__icon { width: 14px; height: 14px; fill: var(--icon); flex: none; }
</style>
</head>
<body>
  <section class="card card--front">
    <div class="brand brand--hero"><span class="brand__mark"></span>Quorvant</div>
    <div class="front__url"><span class="front__rule"></span>www.quorvant.com<span class="front__rule"></span></div>
  </section>

  <section class="card card--back">
    <div class="brand brand--header"><span class="brand__mark"></span>Quorvant</div>

    <div class="person">
      <span class="person__name">Daniel Harrow</span>
      <span class="person__title">Managing Director</span>
    </div>

    <div class="contact contact--row1">
      <span class="contact__item">
        <svg class="contact__icon" viewBox="0 0 16 16"><path d="M2 5c0-2 2-3 6-3s6 1 6 3v1h-3V5H5v1H2z"/><rect x="3" y="8" width="10" height="6" rx="1"/></svg>
        000-111-1111
      </span>
      <span class="contact__item">
        <svg class="contact__icon" viewBox="0 0 16 16"><path d="M1 3h14v10H1z M2 4l6 5 6-5" fill="none" stroke="#8a8a8a" stroke-width="1.5"/></svg>
        daniel@quorvant.com
      </span>
      <span class="contact__item">
        <svg class="contact__icon" viewBox="0 0 16 16"><g fill="none" stroke="#8a8a8a" stroke-width="1.3"><circle cx="8" cy="8" r="6.5"/><ellipse cx="8" cy="8" rx="3" ry="6.5"/><path d="M1.5 8h13M2.5 4.5h11M2.5 11.5h11"/></g></svg>
        www.quorvant.com
      </span>
    </div>

    <div class="contact contact--row2">
      <span class="contact__item">
        <svg class="contact__icon" viewBox="0 0 16 16"><path d="M8 1a5 5 0 0 0-5 5c0 4 5 9 5 9s5-5 5-9a5 5 0 0 0-5-5zm0 7a2 2 0 1 1 0-4 2 2 0 0 1 0 4z"/></svg>
        234 Anywhere St., Any City, Any Town, US 123456
      </span>
    </div>
  </section>
</body>
</html>
```